Commercial Auto Insurance Application and Commercial Property Insurance Application

Hi I need a fillable application for my business to send to potential clients for Commercial Auto Insurance and Commercial Property Insurance. I have attached an example application I currently use for another line of insurance.
Commercial Auto Insurance Application
On the first page I would need the following:
- Business Name: (fill in area for text)
- Effective Date: (fill in area for text)
- How do you structure your business? (Check box for “Sole Proprietor”, “Partnership”, “Corporation”, “LLC”)
- Contact Name: (fill in area for text) / Phone Number: (fill in area for text) / Contact Email (fill in area for text)
- Mailing address: (fill in area for text)
- Garaging location: (fill in area for text)
- Owner Name: (fill in area for text)
- Description of Operations: (fill in area for text)
- How long has the operation been in business? (fill in area for text)
- How many years of experience does your management have in the truck/transportation industry? (fill in area for text)
Coverages
Liability Combined Single Limit: ($1,000,000 (checkbox) / $500,000 (checkbox / $300,000 (checkbox) / Other: (fill in area for text)
Uninsured Motorist CSL: (fill in area for text) (checkbox for “Rejected”)
Medical Payments: (fill in area for text)
Physical Damage: (fill in area for text) (checkbox for Rejected)
Liability Deducible: ($500 checkbox, $1,000 checkbox, $2,500 checkbox, $5,000 checkbox)
Physical Damage Deductible: ($500 checkbox, $1,000 checkbox, $2,500 checkbox, $5,000 checkbox)
Driving radius: (fill in area for text)
How many years have you had your own continuous commercial auto insurance coverage for the current business name? (fill in area for text)
Do any of your vehicles travel across state lines? Yes (checkbox)/ No (checkbox)
If yes, please list all states in which vehicles operate: (fill in area for text)
What is the maximum radius traveled for your customer's business?
0-25 miles (checkbox)
26-50 miles (checkbox)
51-75 miles (checkbox)
76-100 miles (checkbox)
101-150 miles (checkbox)
151-200 miles (checkbox)
201-300 miles (checkbox)
300+ miles (checkbox)
Would you like physical damage coverage for this vehicle? (should be for each vehicle listed)
On the 2nd page of the application I would need the following:
I would need to have it where people can fill in the vehicle information such as VIN:, Year:, Make:, Model:, Type of Vehicle:, Trailers:, Value:
I would also need to have it where people can fill in the drivers with their driver info including Name:, DOB:, DL #:, DL State:, Class of License:, Married: Yes/No, Number of years driving similar vehicle:
Please make it where you can fill in 20 vehicle's information and 20 driver's info.
For the 2nd Application I would need one for Property Insurance
On the Commercial Property Application I would need the following:
- Building Address: (fill in area for text)
- Building Description: (fill in area for text)
- Building Amount: $(fill in area for text)
- Business Personal Property Amount: $ (fill in area for text) (checkbox for Not Needed)
- Building Sq Ft: (fill in area for text)
- Total Area Sq Ft: (fill in area for text)
- Building Construction Type: Wood Frame (checkbox), Steel (checkbox), Fire Resistive (checkbox), Non-Combustible (checkbox), Other (fill in area for text)
- # of stories: (fill in area for text)
- Year Built: (fill in area for text)
- Wiring improvement year: (fill in area for text)
- Roofing improvement year: (fill in area for text)
- Plumbing improvement year: (fill in area for text)
- Heating improvement year: (fill in area for text)
- What is to the right of the building and distance: (fill in area for text)
- What is to the left of the building and distance: (fill in area for text)
- What is in front of the building and distance: (fill in area for text)
- What is behind the building and distance: (fill in area for text)
- Burglar alarm installation and serviced by: (fill in area for text) None (checkbox)
- Does the premises have fire protection? Sprinkler system (checkbox), Fire detection (checkbox), Other: (fill in area for text) None (checkbox)

```html
<!DOCTYPE html>
<html lang="en">
<head>
<meta charset="utf-8">
<title>Commercial Auto &amp; Property Insurance Application</title>
<link href="https://fonts.googleapis.com/css2?family=Open+Sans:wght@400;600;700&family=Roboto+Condensed:wght@700&display=swap" rel="stylesheet">
<style>
:root{
  --navy:#27397d;
  --green:#1e9a4b;
  --ink:#2c3a6e;
  --tint:#d6e4f1;
  --veh-head:#0b79bd;
  --drv-head:#137d3c;
  --rule:#7c879b;
  --cell:#b5bfcc;
  --stage:#eef0f3;
  --band:linear-gradient(90deg,var(--navy) 0%,#24527a 45%,var(--green) 100%);
}
*{box-sizing:border-box;margin:0;padding:0}
html,body{width:1200px;height:793px;overflow:hidden}
body{background:var(--stage);font-family:"Open Sans",sans-serif;color:var(--ink);position:relative}
.page{position:absolute;top:95px;width:472px;height:610px;background:#fff;box-shadow:0 2px 8px rgba(0,0,0,.18);overflow:hidden}
.page-property{left:129px}
.page-auto{left:642px}
.tint{position:absolute;left:0;right:0;background:var(--tint)}
.band{position:absolute;left:0;right:0;background:var(--band);color:#fff}
.section-title{position:absolute;font-weight:700;color:var(--navy);font-size:15.5px;letter-spacing:.2px}

/* tables */
.grid{position:absolute;display:grid;column-gap:1.5px;row-gap:2px}
.grid .h{height:18px;color:#fff;font-size:6.4px;font-weight:600;line-height:1.05;display:flex;align-items:center;justify-content:center;text-align:center}
.grid .h.small{font-size:5.2px}
.vehicles{left:18px;top:39px;grid-template-columns:28.5px 23px 18.5px 43.5px 26px 31px 32px;grid-auto-rows:13.5px}
.vehicles .h{background:var(--veh-head)}
.drivers{left:246px;top:39px;grid-template-columns:26px 22.5px 25.5px 40.5px 26px 63px;grid-auto-rows:13.5px}
.drivers .h{background:var(--drv-head)}
.grid{grid-template-rows:18px}
.c{display:block;border:.6px solid var(--cell);border-radius:1.5px;background:#fff}
.divider{position:absolute;left:235.5px;top:39px;width:1.5px;height:311px;background:var(--tint)}

/* fields */
.row{position:absolute;display:flex;align-items:flex-end;font-size:7.5px;line-height:10px;height:10px;white-space:nowrap;gap:3px}
.line{flex:1;border-bottom:.6px solid var(--rule);margin-bottom:2px;min-width:8px}
.box{display:inline-block;width:9.5px;height:9.5px;border:.6px solid #8d97a8;border-radius:1.5px;background:#fff;vertical-align:middle;flex:none}
.opt{display:inline-flex;align-items:center;gap:2.5px}
.slash{margin:0 1px}

.brand{font-weight:700;color:var(--navy);text-align:center;position:absolute;left:0;right:0}
.brand-mark{display:inline-block;width:9px;height:9px;background:var(--green);margin-right:6px;vertical-align:middle}
.address{position:absolute;left:0;right:0;top:80px;text-align:center;font-size:9.4px;color:var(--navy)}
.app-title{top:106px;height:29.5px;font-family:"Roboto Condensed",sans-serif;font-size:19px;text-align:center;line-height:29.5px;letter-spacing:.4px}
.sub-band{height:18px;line-height:18px;font-weight:700}
.answer-box{position:absolute;left:270px;top:453.5px;width:179px;height:17px;border:.6px solid #8d97a8;border-radius:4px;background:#f1f3f6}
.footer-url{position:absolute;left:24px;top:593px;font-size:7.4px;color:#fff;font-weight:600;letter-spacing:.4px}
</style>
</head>
<body>

<!-- Property / vehicles & drivers page -->
<section class="page page-property">
  <div class="tint" style="top:0;height:47px"></div>
  <h2 class="section-title" style="left:57px;top:18px">VEHICLE INFO</h2>
  <h2 class="section-title" style="left:303px;top:17px">DRIVER&nbsp; INFO</h2>

  <div class="grid vehicles">
    <div class="h">Make</div><div class="h">Model</div><div class="h">Year</div><div class="h">VIN</div><div class="h small">Type of<br>Vehicle</div><div class="h">Trailers</div><div class="h">Value</div>
    <i class="c"></i><i class="c"></i><i class="c"></i><i class="c"></i><i class="c"></i><i class="c"></i><i class="c"></i>
    <i class="c"></i><i class="c"></i><i class="c"></i><i class="c"></i><i class="c"></i><i class="c"></i><i class="c"></i>
    <i class="c"></i><i class="c"></i><i class="c"></i><i class="c"></i><i class="c"></i><i class="c"></i><i class="c"></i>
    <i class="c"></i><i class="c"></i><i class="c"></i><i class="c"></i><i class="c"></i><i class="c"></i><i class="c"></i>
    <i class="c"></i><i class="c"></i><i class="c"></i><i class="c"></i><i class="c"></i><i class="c"></i><i class="c"></i>
    <i class="c"></i><i class="c"></i><i class="c"></i><i class="c"></i><i class="c"></i><i class="c"></i><i class="c"></i>
    <i class="c"></i><i class="c"></i><i class="c"></i><i class="c"></i><i class="c"></i><i class="c"></i><i class="c"></i>
    <i class="c"></i><i class="c"></i><i class="c"></i><i class="c"></i><i class="c"></i><i class="c"></i><i class="c"></i>
    <i class="c"></i><i class="c"></i><i class="c"></i><i class="c"></i><i class="c"></i><i class="c"></i><i class="c"></i>
    <i class="c"></i><i class="c"></i><i class="c"></i><i class="c"></i><i class="c"></i><i class="c"></i><i class="c"></i>
    <i class="c"></i><i class="c"></i><i class="c"></i><i class="c"></i><i class="c"></i><i class="c"></i><i class="c"></i>
    <i class="c"></i><i class="c"></i><i class="c"></i><i class="c"></i><i class="c"></i><i class="c"></i><i class="c"></i>
    <i class="c"></i><i class="c"></i><i class="c"></i><i class="c"></i><i class="c"></i><i class="c"></i><i class="c"></i>
    <i class="c"></i><i class="c"></i><i class="c"></i><i class="c"></i><i class="c"></i><i class="c"></i><i class="c"></i>
    <i class="c"></i><i class="c"></i><i class="c"></i><i class="c"></i><i class="c"></i><i class="c"></i><i class="c"></i>
    <i class="c"></i><i class="c"></i><i class="c"></i><i class="c"></i><i class="c"></i><i class="c"></i><i class="c"></i>
    <i class="c"></i><i class="c"></i><i class="c"></i><i class="c"></i><i class="c"></i><i class="c"></i><i class="c"></i>
    <i class="c"></i><i class="c"></i><i class="c"></i><i class="c"></i><i class="c"></i><i class="c"></i><i class="c"></i>
    <i class="c"></i><i class="c"></i><i class="c"></i><i class="c"></i><i class="c"></i><i class="c"></i><i class="c"></i>
  </div>

  <div class="divider"></div>

  <div class="grid drivers">
    <div class="h">DOB</div><div class="h">DL#</div><div class="h">DL<br>State</div><div class="h">Class of<br>License</div><div class="h small">Married<br>Yes / No</div><div class="h small">Number of years<br>driving similar vehicle</div>
    <i class="c"></i><i class="c"></i><i class="c"></i><i class="c"></i><i class="c"></i><i class="c"></i>
    <i class="c"></i><i class="c"></i><i class="c"></i><i class="c"></i><i class="c"></i><i class="c"></i>
    <i class="c"></i><i class="c"></i><i class="c"></i><i class="c"></i><i class="c"></i><i class="c"></i>
    <i class="c"></i><i class="c"></i><i class="c"></i><i class="c"></i><i class="c"></i><i class="c"></i>
    <i class="c"></i><i class="c"></i><i class="c"></i><i class="c"></i><i class="c"></i><i class="c"></i>
    <i class="c"></i><i class="c"></i><i class="c"></i><i class="c"></i><i class="c"></i><i class="c"></i>
    <i class="c"></i><i class="c"></i><i class="c"></i><i class="c"></i><i class="c"></i><i class="c"></i>
    <i class="c"></i><i class="c"></i><i class="c"></i><i class="c"></i><i class="c"></i><i class="c"></i>
    <i class="c"></i><i class="c"></i><i class="c"></i><i class="c"></i><i class="c"></i><i class="c"></i>
    <i class="c"></i><i class="c"></i><i class="c"></i><i class="c"></i><i class="c"></i><i class="c"></i>
    <i class="c"></i><i class="c"></i><i class="c"></i><i class="c"></i><i class="c"></i><i class="c"></i>
    <i class="c"></i><i class="c"></i><i class="c"></i><i class="c"></i><i class="c"></i><i class="c"></i>
    <i class="c"></i><i class="c"></i><i class="c"></i><i class="c"></i><i class="c"></i><i class="c"></i>
    <i class="c"></i><i class="c"></i><i class="c"></i><i class="c"></i><i class="c"></i><i class="c"></i>
    <i class="c"></i><i class="c"></i><i class="c"></i><i class="c"></i><i class="c"></i><i class="c"></i>
    <i class="c"></i><i class="c"></i><i class="c"></i><i class="c"></i><i class="c"></i><i class="c"></i>
    <i class="c"></i><i class="c"></i><i class="c"></i><i class="c"></i><i class="c"></i><i class="c"></i>
    <i class="c"></i><i class="c"></i><i class="c"></i><i class="c"></i><i class="c"></i><i class="c"></i>
    <i class="c"></i><i class="c"></i><i class="c"></i><i class="c"></i><i class="c"></i><i class="c"></i>
  </div>

  <div class="band" style="top:356px;height:23px;text-align:center;line-height:23px;font-size:15.5px;font-weight:700">PROPERTY INSURANCE</div>
  <div class="tint" style="top:379px;height:180px"></div>

  <div class="row" style="left:24px;width:215px;top:388px">Business Name:<span class="line"></span></div>
  <div class="row" style="left:246px;width:207px;top:388px">Building Address:<span class="line"></span></div>
  <div class="row" style="left:24px;width:215px;top:400.5px">Building Description:<span class="line"></span></div>
  <div class="row" style="left:245px;width:208px;top:400.5px">Building Amount: $<span class="line"></span></div>
  <div class="row" style="left:24px;width:300px;top:413.5px">Business Personal Property Amount: $<span class="line"></span><span class="opt" style="margin-left:4px"><span class="box"></span>Not Needed</span></div>
  <div class="row" style="left:24px;width:160px;top:426px">Building Sq Ft:<span class="line"></span></div>
  <div class="row" style="left:189px;width:166px;top:426px">Total Area Sq Ft:<span class="line"></span></div>
  <div class="row" style="left:24px;top:439px;gap:4px">Building Construction Type: <span class="opt"><span class="box"></span>Wood Frame</span> <span class="opt" style="margin-left:3px"><span class="box"></span>Steel</span> <span class="opt" style="margin-left:3px"><span class="box"></span>Fire Resistive</span> <span class="opt" style="margin-left:3px"><span class="box"></span>Non-Combustible, Other</span></div>
  <div class="row" style="left:24px;width:215px;top:451.5px"># of stories:<span class="line"></span></div>
  <div class="row" style="left:246px;width:207px;top:451.5px">Year Built:<span class="line"></span></div>
  <div class="row" style="left:24px;width:196px;top:464px">Wiring improvement year:<span class="line"></span></div>
  <div class="row" style="left:223px;width:230px;top:464px">Roofing improvement year:<span class="line"></span></div>
  <div class="row" style="left:24px;width:196px;top:476.5px">Plumbing improvement year:<span class="line"></span></div>
  <div class="row" style="left:223px;width:230px;top:476.5px">Heating improvement year:<span class="line"></span></div>
  <div class="row" style="left:24px;width:429px;top:489px">What is to the right of the building and distance:<span class="line"></span></div>
  <div class="row" style="left:24px;width:429px;top:501.5px">What is to the left of the building and distance:<span class="line"></span></div>
  <div class="row" style="left:24px;width:219px;top:514.5px">What is in front of the building and distance:<span class="line"></span></div>
  <div class="row" style="left:246px;width:207px;top:514.5px">What is behind the building and distance:<span class="line"></span></div>
  <div class="row" style="left:24px;width:316px;top:527px">Burglar alarm installation and serviced by:<span class="line"></span><span class="opt" style="margin-left:8px"><span class="box"></span>None</span></div>
  <div class="row" style="left:24px;width:429px;top:540.5px">Does the premises have fire protection? <span class="opt" style="margin-left:5px"><span class="box"></span>Sprinkler system,</span> <span class="opt" style="margin-left:3px"><span class="box"></span>Fire detection,</span> <span class="opt" style="margin-left:3px"><span class="box"></span>Other:</span><span class="line" style="border:0"></span><span class="opt"><span class="box"></span>None</span></div>

  <div class="brand" style="top:582px;font-size:14px;letter-spacing:1.5px"><span class="brand-mark"></span>PRAIRIEVIEW INSURANCE SERVICES</div>
</section>

<!-- Commercial auto page -->
<section class="page page-auto">
  <div class="brand" style="top:30px;font-size:21px;letter-spacing:.5px;line-height:26px"><span class="brand-mark"></span>PRAIRIEVIEW</div>
  <div class="brand" style="top:57px;font-size:8.6px;letter-spacing:3.2px">INSURANCE SERVICES</div>
  <p class="address">2480 Meridian Ave Suite 310, Lakewood, CA 90712. Tel: (555) 014-2290</p>

  <h1 class="band app-title">COMMERCIAL AUTO INSURANCE APPLICATION</h1>

  <div class="row" style="left:23px;width:280px;top:154px">Business Name:<span class="line"></span></div>
  <div class="row" style="left:307px;width:142px;top:154px">Effective Date:<span class="line"></span></div>
  <div class="row" style="left:23px;top:173.5px;gap:4px">How do you structure your business? <span class="opt" style="margin-left:3px"><span class="box"></span>Sole Proprietor</span> <span class="opt" style="margin-left:3px"><span class="box"></span>Partnership</span> <span class="opt" style="margin-left:3px"><span class="box"></span>Corporation</span> <span class="opt" style="margin-left:3px"><span class="box"></span>LLC</span></div>
  <div class="row" style="left:23px;width:426px;top:195px;gap:2px">Contact Name:<span class="line" style="flex:.75"></span><span class="slash">/</span>Phone Number:<span class="line" style="flex:.75"></span><span class="slash">/</span>Contact Email:<span class="line"></span></div>
  <div class="row" style="left:23px;width:272px;top:217px">Mailing address:<span class="line"></span></div>
  <div class="row" style="left:298px;width:152px;top:217px">Garaging location:<span class="line"></span></div>
  <div class="row" style="left:23px;width:166px;top:237px">Owner Name:<span class="line"></span></div>
  <div class="row" style="left:193px;width:256px;top:237px">Description of Operations<span class="line"></span></div>
  <div class="row" style="left:22px;width:427px;top:257px">How long has the operation been in business?<span class="line"></span></div>
  <div class="row" style="left:23px;width:426px;top:277.5px">How many years of experience does your management have in the truck/transportation industry?<span class="line"></span></div>

  <div class="band sub-band" style="top:298px;padding-left:27px;font-size:11.5px">COVERAGES</div>
  <div class="tint" style="top:316px;height:198.5px"></div>

  <div class="row" style="left:23px;width:426px;top:327.5px;gap:3px">Liability Combined Single Limit: ($1,000,000 <span class="box"></span> / $500,000 <span class="box"></span> / $300,000 <span class="box"></span> / Other:<span class="line" style="margin-left:5px"></span></div>
  <div class="row" style="left:23px;width:382px;top:348px">Uninsured Motorist CSL:<span class="line"></span><span class="opt" style="margin-left:2px"><span class="box"></span>Rejected</span></div>
  <div class="row" style="left:23px;width:340px;top:366.5px">Medical Payments:<span class="line"></span></div>
  <div class="row" style="left:23px;width:382px;top:384px">Physical Damage:<span class="line"></span><span class="opt" style="margin-left:2px"><span class="box"></span>Rejected</span></div>
  <div class="row" style="left:23px;top:400px;gap:3px">Liability Deducible: &nbsp;$500 <span class="box"></span>, $1,000 <span class="box"></span>, $2,500 <span class="box"></span>, $5,000 <span class="box"></span></div>
  <div class="row" style="left:23px;top:419px;gap:3px">Physical Damage Deductible: $500 <span class="box"></span>, $1,000 <span class="box"></span>, $2,500 <span class="box"></span>, $5,000 <span class="box"></span></div>
  <div class="row" style="left:23px;width:426px;top:436px">Driving radius:<span class="line"></span></div>
  <div class="row" style="left:23px;top:450px;height:20px;line-height:9px;align-items:flex-start">How many years have you had your own continuous<br>commercial auto insurance coverage for the current business name?</div>
  <div class="answer-box"></div>
  <div class="row" style="left:23px;top:477px;gap:3px">Do any of your vehicles travel across state lines? &nbsp;Yes <span class="box"></span>/ No <span class="box"></span></div>
  <div class="row" style="left:23px;width:426px;top:496px">If yes, please list all states in which vehicles operate:<span class="line"></span></div>

  <div class="band" style="top:514.5px;height:18px;line-height:18px;padding-left:27px;font-size:7.8px;font-weight:700">What is the maximum radius traveled for your customer's business?</div>

  <div class="row" style="left:25px;top:536px"><span class="opt"><span class="box"></span>0-25 miles</span></div>
  <div class="row" style="left:94px;top:536px"><span class="opt"><span class="box"></span>26-50 miles</span></div>
  <div class="row" style="left:167px;top:536px"><span class="opt"><span class="box"></span>51-75 miles</span></div>
  <div class="row" style="left:232.5px;top:536px"><span class="opt"><span class="box"></span>76-100 miles</span></div>
  <div class="row" style="left:25px;top:549.5px"><span class="opt"><span class="box"></span>101-150 miles</span></div>
  <div class="row" style="left:94px;top:549.5px"><span class="opt"><span class="box"></span>151-200 miles</span></div>
  <div class="row" style="left:167px;top:549.5px"><span class="opt"><span class="box"></span>201-300 miles</span></div>
  <div class="row" style="left:232.5px;top:549.5px"><span class="opt"><span class="box"></span>300+ miles</span></div>

  <div class="row" style="left:24px;top:570px">Would you like physical damage coverage for this vehicle? (should be for each vehicle listed)</div>

  <svg style="position:absolute;left:0;top:591px" width="472" height="19" viewBox="0 0 472 19" aria-hidden="true">
    <defs>
      <linearGradient id="footer-strip" x1="0" x2="1">
        <stop offset="0" stop-color="#1e9a4b"/>
        <stop offset="1" stop-color="#27397d"/>
      </linearGradient>
    </defs>
    <rect x="180" y="11" width="292" height="8" fill="url(#footer-strip)"/>
    <polygon points="0,0 197,0 184,19 0,19" fill="#27397d"/>
  </svg>
  <p class="footer-url">www.PrairieviewInsuranceServices.com</p>
</section>

</body>
</html>
```